Brenna's Wine Label Design

Design for a wine bottle label. It'Is for A Dog Bar. This bar is upscale, so I am going for an elegant look
Here is what I am requesting.
1.Label to fit a wine bottle 4" Wide x 5" Length
1. Black Matte or Slate if you if you are having trouble with colors
2. The writing done in Gold Foil
3. Please consider the what the logo looks like- also it has a copy write on the art. If you can insert that it would be nicel
4. Please have print the says the "Pup Warden's Pick"
5. Please Incorporate Coral Dune Beach Florida
www.brennacastavelt.example and 555-318-9062
5. Product de France
4. Please incorporate the photo of the dog attached
6. I have added a couple of example label photos to give you an idea of the feel of the look I am seeking
7.One Type of wine is Chardonnay
8.One type of wine is Pinot Noir
8. Notice the image with the dog paw incorporate in the scroll work. Love that!

Target Market(s)

Dog and Upscale Wine lovers

Font styles to use
Decorative
Script

Requirements
Must have
• See Project Description
Nice to have
• Copy right symbol after logo

```html
<!DOCTYPE html>
<html lang="en">
<head>
<meta charset="utf-8">
<title>Brenna's Wine Labels</title>
<link href="https://fonts.googleapis.com/css2?family=Cinzel:wght@400;500&family=Tinos:wght@400;700&display=swap" rel="stylesheet">
<style>
  :root {
    --bg-top: #b4b4b4;
    --bg-bottom: #f4f4f4;
    --slate: #121212;
    --cream: #dcdad3;
    --gold: #c9a862;
    --gold-deep: #8e7440;
    --gold-light: #e8d39c;
    --photo-dark: #2c2c2c;
    --photo-light: #b9b9b9;
    --band-ink: #1a1a1a;
  }
  * { box-sizing: border-box; margin: 0; padding: 0; }
  html, body { width: 1200px; height: 1200px; overflow: hidden; }
  body {
    background: linear-gradient(var(--bg-top), var(--bg-bottom));
    display: flex;
    justify-content: center;
    align-items: center;
    gap: 80px;
  }
  .label {
    width: 420px;
    height: 560px;
    display: flex;
    flex-direction: column;
    align-items: center;
    padding-top: 34px;
    position: relative;
  }
  .label--red { background: var(--slate); --ink: var(--gold); --ink-soft: var(--gold-light); }
  .label--white { background: var(--cream); --ink: var(--gold-deep); --ink-soft: var(--gold-deep); }

  .brand-mark {
    width: 50px; height: 50px;
    border: 2px solid var(--ink);
    border-radius: 50%;
  }
  .ornament {
    display: block;
    height: 6px;
    background: linear-gradient(90deg, transparent, var(--ink), transparent);
    opacity: .8;
  }
  .ornament--wide { width: 300px; margin-top: 8px; }
  .ornament--mid { width: 220px; margin: 8px 0; }
  .brand-name {
    font-family: "Cinzel", serif;
    font-weight: 400;
    color: var(--ink);
    text-align: center;
    line-height: 1;
    margin-top: 10px;
  }
  .brand-name__first { font-size: 30px; letter-spacing: 2px; display: block; }
  .brand-name__last { font-size: 15px; letter-spacing: 6px; display: block; margin-top: 4px; }
  .dog-photo {
    width: 150px; height: 150px;
    margin-top: 10px;
    background: linear-gradient(160deg, var(--photo-light), var(--photo-dark));
  }
  .tagline {
    font-family: "Cinzel", serif;
    font-weight: 400;
    font-size: 13px;
    color: var(--ink);
    margin-top: 14px;
    letter-spacing: .5px;
  }
  .varietal {
    font-family: "Cinzel", serif;
    font-weight: 400;
    font-size: 36px;
    letter-spacing: 3px;
    color: var(--ink-soft);
    line-height: 1;
  }
  .details {
    font-family: "Tinos", serif;
    color: #f2f2f2;
    text-align: center;
    font-size: 13px;
    line-height: 1.45;
    margin-top: 4px;
  }
  .label--white .details { color: #3a3a3a; }
  .details__place { letter-spacing: 1.5px; }
  .origin-band {
    position: absolute;
    left: 0; right: 0; bottom: 0;
    height: 22px;
    background: linear-gradient(90deg, var(--gold-deep), var(--gold-light) 50%, var(--gold-deep));
    font-family: "Tinos", serif;
    font-size: 14px;
    color: var(--band-ink);
    text-align: center;
    line-height: 22px;
  }
</style>
</head>
<body>
  <section class="label label--red">
    <span class="brand-mark"></span>
    <span class="ornament ornament--wide" role="img" aria-label="Gold scrollwork flourish"></span>
    <h1 class="brand-name"><span class="brand-name__first">BRENNA</span><span class="brand-name__last">CASTAVELT</span></h1>
    <span class="ornament ornament--mid" role="img" aria-label="Gold scrollwork flourish"></span>
    <div class="dog-photo" role="img" aria-label="Black and white photo of the bar's dog wearing a flat cap"></div>
    <p class="tagline">Pup Warden's Pick</p>
    <span class="ornament ornament--mid" role="img" aria-label="Gold scrollwork flourish"></span>
    <h2 class="varietal">PINOT NOIR</h2>
    <span class="ornament ornament--mid" role="img" aria-label="Gold scrollwork flourish"></span>
    <p class="details"><span class="details__place">Coral Dune Beach Florida</span><br>www.brennacastavelt.example<br>555-318-9062</p>
    <div class="origin-band">Product de France</div>
  </section>

  <section class="label label--white">
    <span class="brand-mark"></span>
    <span class="ornament ornament--wide" role="img" aria-label="Gold scrollwork flourish"></span>
    <h1 class="brand-name"><span class="brand-name__first">BRENNA</span><span class="brand-name__last">CASTAVELT</span></h1>
    <span class="ornament ornament--mid" role="img" aria-label="Gold scrollwork flourish"></span>
    <div class="dog-photo" role="img" aria-label="Black and white photo of the bar's dog wearing a flat cap"></div>
    <p class="tagline">Pup Warden's Pick</p>
    <span class="ornament ornament--mid" role="img" aria-label="Gold scrollwork flourish"></span>
    <h2 class="varietal">CHARDONNAY</h2>
    <span class="ornament ornament--mid" role="img" aria-label="Gold scrollwork flourish"></span>
    <p class="details"><span class="details__place">Coral Dune Beach Florida</span><br>www.brennacastavelt.example<br>555-318-9062</p>
    <div class="origin-band">Product de France</div>
  </section>
</body>
</html>
```